Chairside Roots: the dental helper's field guide, start to finish

Book cover:

Book about dental implantology
Reader is a dental assistant
Introduction to surgical knowledge to case acceptance. We will start with the intro to implants that will cover population stats on tooth loss, how to make the patient trust the team, how to communicate with the patient. Then we will get more technical; bone loss, bone quality and quantity. We will also inform on pros and cons of different classic dental treatments vs implant treatment. Surgical knowledge deep into various aspects of implants procedures. An illustration of surgical instruments needed and motors and hand pieces. Operatory set up will be demonstrated. I’ll be guiding the role of the surgical assistant and non surgical assistant. At the end I’ll explain how to close an implant case. From single implants to more complex cases.

Target Market(s)

Dental assistants

Industry/Entity Type

Dental

Font styles to use
Other font styles liked:
• Mellifluous or addington

Colors
EE7325
F08F49
F5BC92
FAE3D3
FDF4ED

Requirements
Must have
• Dental implant, positive vibe, orange Colors, professional
Nice to have
• Sense of team spirit, uncluttered,
Should not have
• Images of people

```html
<!DOCTYPE html>
<html lang="en">
<head>
<meta charset="utf-8">
<title>Chairside Roots – Book Cover</title>
<link rel="stylesheet" href="https://fonts.googleapis.com/css2?family=Oswald:wght@400;600&family=Tinos&display=swap">
<style>
  :root {
    --orange: #EE7325;
    --orange-mid: #F08F49;
    --orange-soft: #F5BC92;
    --peach: #FAE3D3;
    --cream: #FDF4ED;
    --red-orange: #D93C18;
    --ink: #1A1A1A;
    --white: #FFFFFF;
  }
  html, body {
    margin: 0;
    padding: 0;
    overflow: hidden;
    background: var(--white);
  }
  .cover-wrap {
    position: relative;
    width: 1200px;
    height: 903px;
    overflow: hidden;
    background: var(--orange);
  }
  .back-cover {
    position: absolute;
    left: 0;
    top: 0;
    width: 637px;
    height: 903px;
    background: var(--orange);
  }
  .blurb {
    position: absolute;
    left: 64px;
    top: 112px;
    width: 439px;
    margin: 0;
    font-family: "Tinos", "Times New Roman", serif;
    font-size: 18.4px;
    line-height: 22.2px;
    color: var(--white);
    text-align: justify;
  }
  .blurb p { margin: 0; }
  .isbn-box {
    position: absolute;
    left: 374px;
    top: 789px;
    width: 129px;
    height: 75px;
    background: var(--white);
  }
  .spine-title {
    position: absolute;
    left: 580px;
    top: 118px;
    margin: 0;
    writing-mode: vertical-rl;
    font-family: "Oswald", sans-serif;
    font-weight: 600;
    font-size: 42px;
    line-height: 1;
    letter-spacing: 1px;
    color: var(--white);
    white-space: nowrap;
  }
  .front-cover {
    position: absolute;
    left: 637px;
    top: 0;
    width: 563px;
    height: 903px;
    background: var(--cream);
  }
  .front-shapes {
    position: absolute;
    inset: 0;
  }
  .title {
    position: absolute;
    right: 42px;
    top: 34px;
    margin: 0;
    font-family: "Oswald", sans-serif;
    font-weight: 600;
    font-size: 59px;
    line-height: 70px;
    color: var(--orange);
    text-align: right;
    letter-spacing: 0.5px;
  }
  .subtitle {
    position: absolute;
    right: 42px;
    top: 180px;
    margin: 0;
    font-family: "Oswald", sans-serif;
    font-weight: 400;
    font-size: 33px;
    line-height: 48px;
    color: var(--ink);
    text-align: right;
    letter-spacing: -0.3px;
  }
  .implant-art {
    position: absolute;
    left: 218px;
    top: 451px;
    width: 250px;
    height: 393px;
    background: linear-gradient(180deg, var(--orange) 0%, var(--orange-mid) 55%, var(--orange) 100%);
  }
</style>
</head>
<body>
<main class="cover-wrap">
  <section class="back-cover">
    <div class="blurb">
      <p>Lorem ipsum dolor sit amet, consectetuer adipiscing elit, sed diam nonummy nibh euismod tincidunt ut laoreet dolore magna aliquam erat volutpat. Ut wisi enim ad minim veniam, quis nostrud exerci tation ullamcorper suscipit lobortis nisl ut aliquip ex ea commodo consequat. Duis autem vel eum iriure dolor in hendrerit in vulputate velit esse molestie consequat, vel illum dolore eu feugiat nulla facilisis at vero eros et accumsan et iusto odio dignissim qui blandit praesent luptatum zzril delenit augue duis dolore te feugait nulla facilisi.</p>
      <p>Lorem ipsum dolor sit amet, cons ectetuer adipiscing elit, sed diam nonummy nibh euismod tincidunt ut laoreet dolore magna aliquam erat volutpat. Ut wisi enim ad minim veniam, quis nostrud exerci tation ullamcorper suscipit lobortis nisl ut aliquip ex ea commodo consequat.</p>
      <p>Lorem ipsum dolor sit amet, consectetuer adipiscing elit, sed diam nonummy nibh euismod tincidunt ut laoreet dolore magna aliquam erat volutpat. Ut wisi enim ad minim veniam, quis nostrud exerci tation ullamcorper suscipit lobortis nisl ut aliquip ex ea commodo consequat. Duis autem vel eum iriure dolor in hendrerit in vulputate velit esse molestie consequat, vel illum dolore eu feugiat nulla facilisis at vero eros et accumsan et iusto odio dignissim qui blandit praesent luptatum zzril delenit augue duis dolore te feugait nulla facilisi.</p>
      <p>Lorem ipsum dolor sit amet, cons ectetuer adipiscing elit,</p>
    </div>
    <div class="isbn-box"></div>
    <h2 class="spine-title">CHAIRSIDE&nbsp; ROOTS</h2>
  </section>

  <section class="front-cover">
    <svg class="front-shapes" width="563" height="903" viewBox="0 0 563 903" xmlns="http://www.w3.org/2000/svg" aria-hidden="true">
      <defs>
        <linearGradient id="band-light" x1="0" y1="0" x2="1" y2="0">
          <stop offset="0" stop-color="#F08F49"/>
          <stop offset="0.45" stop-color="#FAE3D3"/>
          <stop offset="1" stop-color="#F08F49"/>
        </linearGradient>
        <linearGradient id="band-soft" x1="0" y1="0" x2="1" y2="0">
          <stop offset="0" stop-color="#F5BC92"/>
          <stop offset="0.6" stop-color="#FDF4ED"/>
          <stop offset="1" stop-color="#F5BC92"/>
        </linearGradient>
      </defs>
      <path d="M0 221 C90 215 170 300 240 335 C320 372 420 345 563 272 L563 903 L0 903 Z" fill="#F08F49"/>
      <path d="M0 316 C90 300 180 330 250 350 C330 370 450 360 563 320 L563 903 L0 903 Z" fill="url(#band-soft)"/>
      <path d="M0 450 C60 380 170 360 260 372 C350 385 460 380 563 340 L563 903 L0 903 Z" fill="url(#band-light)"/>
      <path d="M0 450 C70 395 180 372 300 376 C400 380 480 365 563 338 L563 903 L0 903 Z" fill="#EE7325"/>
      <path d="M313 385 C380 395 470 370 563 340 L563 903 L53 903 C40 820 30 720 55 640 C85 540 190 420 313 385 Z" fill="#D93C18"/>
    </svg>

    <h1 class="title">CHAIRSIDE<br>ROOTS</h1>
    <p class="subtitle">Passionate Teams Deliver Life-Changing<br>Patient Experiences</p>

    <div class="implant-art" role="img" aria-label="Illustration of a dental implant: a white crown on a threaded metal screw, set on a brushed orange patch"></div>
  </section>
</main>
</body>
</html>
```